Creation of a cover for the book "A lantern beneath the pines" with the painting "Le quai.tif" enclosed; a romantic, sensual story of a young woman.
Size of the book: 14 x 20.5 cm
Title: "A lantern beneath the pines"
Author: "Corinne Valmont"
Publisher: "Marrow Editions" (at the bottom of the page).
Updates
Waiting for the author to be available
Waiting for the author to be available. Please apologize
Target Market(s)
general public
Industry/Entity Type
Book
Look and feel
Each slider illustrates characteristics of the customer's brand and the style your logo design should communicate.

```html
<!DOCTYPE html>
<html lang="en">
<head>
<meta charset="utf-8">
<title>A lantern beneath the pines — Corinne Valmont</title>
<link rel="stylesheet" href="https://fonts.googleapis.com/css2?family=Italiana&family=Allura&family=Montserrat:wght@400;500&family=Playfair+Display:wght@800&display=swap">
<style>
  :root {
    --sky-top: #7a1f22;
    --sky-mid: #962428;
    --sky-low: #a4282a;
    --ink: #ffffff;
    --paint-dark: #2a2f3a;
    --paint-grey: #8d97a3;
    --paint-skin: #d9b3a0;
    --name-silver: #dfe2e6;
  }
  * { margin: 0; padding: 0; box-sizing: border-box; }
  html, body { width: 822px; height: 1200px; overflow: hidden; }
  body { background: var(--sky-mid); }
  .cover {
    position: relative;
    width: 822px;
    height: 1200px;
    overflow: hidden;
    background:
      radial-gradient(ellipse 70% 20% at 30% 12%, rgba(160,60,60,.35), transparent 70%),
      radial-gradient(ellipse 80% 15% at 70% 40%, rgba(120,25,30,.4), transparent 70%),
      linear-gradient(180deg, var(--sky-top) 0%, var(--sky-mid) 45%, var(--sky-low) 100%);
    color: var(--ink);
  }
  .title {
    position: absolute;
    left: 0; right: 0; top: 32px;
    text-align: center;
    font-family: "Italiana", serif;
    font-weight: 400;
    line-height: 1;
  }
  .title-line { display: block; font-size: 92px; letter-spacing: 0; }
  .title-line--second { font-size: 82px; margin-top: 22px; }
  .title-joiner {
    font-family: "Allura", cursive;
    font-size: 46px;
    vertical-align: 16px;
    margin: 0 2px;
  }
  .kicker {
    position: absolute;
    left: 0; right: 0; top: 257px;
    text-align: center;
    font-family: "Montserrat", sans-serif;
    font-size: 19px;
    letter-spacing: 5px;
  }
  .byline {
    position: absolute;
    left: 0; right: 0; top: 296px;
    text-align: center;
    font-family: "Montserrat", sans-serif;
    font-weight: 500;
    font-size: 20px;
    letter-spacing: 4.6px;
  }
  .frame { position: absolute; left: 0; top: 0; }
  .painting-name {
    position: absolute;
    left: 340px; top: 466px;
    width: 230px;
    text-align: center;
    font-family: "Playfair Display", serif;
    font-weight: 800;
    color: var(--name-silver);
    line-height: 1.2;
    font-size: 38px;
    letter-spacing: 1px;
  }
  .publisher {
    position: absolute;
    left: 0; right: 0; top: 1152px;
    text-align: center;
    font-family: "Montserrat", sans-serif;
    font-size: 20px;
    letter-spacing: 11px;
  }
</style>
</head>
<body>
<main class="cover">
  <h1 class="title">
    <span class="title-line">A lantern</span>
    <span class="title-line title-line--second">beneath <span class="title-joiner">the</span> pines</span>
  </h1>
  <p class="kicker">A BOOK</p>
  <p class="byline">by Corinne Valmont</p>

  <svg class="frame" width="822" height="1200" viewBox="0 0 822 1200">
    <defs>
      <clipPath id="painting-arch">
        <path d="M200,1108 V616 A211,211 0 0 1 622,616 V1108 Z"/>
      </clipPath>
      <linearGradient id="painting-tones" x1="0" y1="0" x2="1" y2="1">
        <stop offset="0" stop-color="var(--paint-grey)"/>
        <stop offset="0.35" stop-color="var(--paint-skin)"/>
        <stop offset="0.6" stop-color="var(--paint-dark)"/>
        <stop offset="1" stop-color="var(--paint-dark)"/>
      </linearGradient>
    </defs>
    <path class="arch-outline" d="M166,1138 V617 A245,245 0 0 1 656,617 V1138 Z"
          fill="none" stroke="var(--ink)" stroke-width="1.5"/>
    <g clip-path="url(#painting-arch)">
      <rect class="painting" x="200" y="405" width="422" height="703"
            fill="url(#painting-tones)" role="img"
            aria-label="Cover painting in grey, warm skin and dark tones with red accents"/>
    </g>
    <path class="arch-inner" d="M200,1108 V616 A211,211 0 0 1 622,616 V1108 Z"
          fill="none" stroke="var(--ink)" stroke-width="1.5"/>
    <path class="sparkle" d="M655,636 Q658,654 676,657 Q658,660 655,678 Q652,660 634,657 Q652,654 655,636 Z" fill="var(--ink)"/>
    <path class="sparkle" d="M167,921 Q170,939 188,942 Q170,945 167,963 Q164,945 146,942 Q164,939 167,921 Z" fill="var(--ink)"/>
  </svg>

  <p class="painting-name">CORINNE<br>VALMONT</p>

  <p class="publisher">Marrow Editions</p>
</main>
</body>
</html>
```